Label

I need a label designed for a bottle of water. I like the lightning bolt and the blue. But I do not want it exactly like the Zimm-ooh.

The label needs to be 9 inches by 2.5 inches.

Logo Text

Mesa Spring: Sip the Mesa

```html
<!DOCTYPE html>
<html lang="en">
<head>
<meta charset="utf-8">
<title>Mesa Spring – Bottle Label</title>
<link rel="stylesheet" href="https://fonts.googleapis.com/css2?family=Oswald:wght@600&family=Archivo+Black&family=Tinos&display=swap">
<style>
  :root {
    --page: #ffffff;
    --sky-top: #d2f5fb;
    --sky-mid: #86d3f2;
    --sky-low: #3d9be8;
    --sky-bottom: #1775e0;
    --navy: #12265a;
    --pill: #ffffff;
    --tagline: #1b2fd2;
    --volume: #1d2a4a;
  }
  html, body {
    margin: 0;
    padding: 0;
    width: 1200px;
    height: 442px;
    overflow: hidden;
    background: var(--page);
  }
  .canvas {
    position: relative;
    width: 1200px;
    height: 442px;
  }
  .label {
    position: absolute;
    left: 68px;
    top: 75px;
    width: 1054px;
    height: 293px;
    overflow: hidden;
  }
  .label-art {
    position: absolute;
    inset: 0;
    background: linear-gradient(180deg,
      var(--sky-top) 0%,
      var(--sky-mid) 38%,
      var(--sky-low) 72%,
      var(--sky-bottom) 100%);
  }
  .brand-name {
    position: absolute;
    left: 0;
    right: 0;
    top: 52px;
    margin: 0;
    text-align: center;
    font-family: "Oswald", "Arial Narrow", sans-serif;
    font-weight: 600;
    font-size: 104px;
    line-height: 1;
    letter-spacing: 1px;
    color: var(--navy);
    text-transform: uppercase;
  }
  .tagline {
    position: absolute;
    left: 310px;
    top: 205px;
    width: 428px;
    height: 28px;
    border-radius: 14px;
    background: var(--pill);
    margin: 0;
    display: flex;
    align-items: center;
    justify-content: center;
    font-family: "Archivo Black", "Arial Black", sans-serif;
    font-size: 24px;
    letter-spacing: 1px;
    color: var(--tagline);
    text-transform: uppercase;
  }
  .volume {
    position: absolute;
    left: 488px;
    top: 250px;
    margin: 0;
    font-family: "Tinos", "Times New Roman", serif;
    font-size: 18px;
    color: var(--volume);
  }
</style>
</head>
<body>
  <div class="canvas">
    <section class="label">
      <div class="label-art" role="img" aria-label="Water droplets on a blue surface with a pale lightning bolt striking down the centre"></div>
      <h1 class="brand-name">Mesa Spring</h1>
      <p class="tagline">Sip the Mesa</p>
      <p class="volume">1 liter</p>
    </section>
  </div>
</body>
</html>
```